We are full service plumbing contractors that are capable of performing all of your plumbing need...

A clean, crisp website that conveys we can handle any plumbing from drain cleaning, repairs, to new construction. But emphasis on Leak detection, under-slab and underground water service leaks, repairs, and reroutes. Leak detection by acoustical, Thermal, or tracer gas , methods.Also emphasize advanced drain cleaning technologies and equipment. Don't just poke ahole in the drain blockage, Clean the pipe, with our High pressure hydrojetters, or Chain knocker drain cables that expand to the width of the pipe being cleaned.

Number of Pages Required

5+ page

Font styles to use
Sans Serif

Requirements
Should not have
• Canned photos

```html
<!DOCTYPE html>
<html lang="en">
<head>
<meta charset="utf-8">
<title>ClearFlow Plumbing</title>
<link href="https://fonts.googleapis.com/css2?family=Open+Sans:wght@400;600;700;800&display=swap" rel="stylesheet">
<style>
:root{
  --blue:#1b9bd7;
  --blue-dark:#0f7fb5;
  --red:#d9262e;
  --ink:#2d2d2d;
  --muted:#6b6b6b;
  --light:#eef0f3;
  --yellow:#f2b320;
  --night:#26282c;
}
*{box-sizing:border-box;margin:0;padding:0}
html,body{width:1200px;height:4072px;overflow:hidden}
body{font-family:"Open Sans",sans-serif;color:var(--ink);background:#fff;position:relative}
section,header,footer{position:absolute;left:0;width:1200px}
.btn{display:inline-block;font-weight:700;font-size:14px;color:#fff;padding:12px 26px;border-radius:3px;letter-spacing:.5px}
.btn-blue{background:var(--blue)}
.btn-red{background:var(--red)}
.brand{font-weight:800;font-size:34px;color:var(--red);display:flex;align-items:center;gap:10px}
.brand i{display:block;width:18px;height:18px;border-radius:50%;background:var(--blue)}

/* header */
.site-header{top:0;height:120px;background:#fff;z-index:3}
.site-header .brand{position:absolute;left:60px;top:30px}
.topbar{position:absolute;right:40px;top:18px;display:flex;align-items:center;gap:14px;font-size:14px;color:var(--ink)}
.topbar b{color:var(--blue)}
.topbar .phone-ico{width:26px;height:26px;border-radius:50%;background:var(--blue)}
.social{display:flex;gap:8px}
.social span{width:28px;height:28px;border-radius:50%;background:var(--blue)}
.social span:last-child{background:var(--red)}
.main-nav{position:absolute;right:0;top:72px;width:720px;height:48px;background:var(--blue);display:flex;align-items:center;padding-left:30px}
.main-nav a{color:#fff;font-size:13px;font-weight:600;margin-right:30px}
.main-nav .btn-red{margin-left:auto;height:48px;line-height:48px;padding:0 30px;border-radius:0}

/* hero */
.hero{top:0;height:940px;overflow:hidden}
.hero-photo{position:absolute;inset:0;background:linear-gradient(120deg,#6d747c 0%,#9aa1a8 40%,#5f676f 70%,#8b8f94 100%)}
.hero-shade{position:absolute;inset:0;background:linear-gradient(90deg,rgba(20,30,40,.55),rgba(20,30,40,.1))}
.hero-copy{position:absolute;left:40px;top:360px;color:#fff}
.hero-copy h1{font-size:46px;line-height:1.15;font-weight:800;text-transform:uppercase;text-shadow:0 2px 6px rgba(0,0,0,.4)}
.hero-copy p{font-size:16px;margin:14px 0 24px}
.quote-form{position:absolute;left:820px;top:180px;width:340px;background:rgba(27,155,215,.92);padding:0 24px 26px}
.quote-form h2{font-size:20px;color:#fff;text-align:center;font-weight:700;padding:18px 0}
.quote-form .field{height:36px;background:#fff;border-radius:2px;margin-bottom:12px;padding:9px 12px;font-size:12px;color:#999}
.quote-form .field.tall{height:60px}
.quote-form .btn-red{display:block;text-align:center;margin-top:10px}
.hero-wave{position:absolute;left:0;bottom:0}

/* features */
.features{top:940px;height:220px;display:flex;justify-content:center;gap:140px}
.feature{width:240px;text-align:center}
.feature .ico{width:90px;height:90px;border-radius:50%;margin:0 auto 16px;display:flex;align-items:center;justify-content:center}
.feature h3{font-size:14px;font-weight:700;text-transform:uppercase;margin-bottom:8px}
.feature p{font-size:12px;color:var(--muted);line-height:1.6}

/* about */
.about{top:1160px;height:360px;background:var(--light)}
.about-copy{position:absolute;left:40px;top:50px;width:560px}
.about h2{font-size:30px;font-weight:800;color:var(--ink);margin-bottom:14px}
.about h2 span{color:var(--blue)}
.about p{font-size:12.5px;line-height:1.65;color:var(--muted);margin-bottom:12px}
.about-video{position:absolute;left:720px;top:30px;width:330px;height:280px;background:linear-gradient(135deg,#8a7a6c,#5d6670);display:flex;align-items:center;justify-content:center}

/* section titles */
.section-title{text-align:center;font-size:32px;font-weight:800;text-transform:uppercase}
.section-title span{color:var(--blue)}
.title-rule{display:block;margin:10px auto 0}

/* services */
.services{top:1580px;height:520px}
.service-grid{position:absolute;left:140px;top:150px;display:flex;gap:20px}
.service-card{width:215px;text-align:center}
.service-card .photo{height:150px;background:linear-gradient(135deg,#8d949b,#5a6168)}
.service-card h3{font-size:13px;font-weight:700;margin:16px 0 6px;text-transform:uppercase}
.service-card p{font-size:11.5px;color:var(--muted);line-height:1.6}
.service-card .more{width:22px;height:22px;border-radius:50%;background:var(--blue);margin:14px auto 0}

/* why choose */
.why{top:2140px;height:620px;background:linear-gradient(135deg,#3a3d42,#1e2024);color:#fff}
.why .section-title{position:absolute;top:50px;width:100%;color:#fff}
.why-item{position:absolute;width:240px}
.why-item h3{font-size:13px;font-weight:700;text-transform:uppercase;margin-bottom:6px}
.why-item p{font-size:11.5px;line-height:1.6;color:#c9c9c9}
.why-item.left{text-align:right}
.why-map{position:absolute;left:0;top:0}
.why-center{position:absolute;left:470px;top:250px;width:260px;height:260px;border-radius:50%;background:#fff;border:10px solid var(--yellow);display:flex;align-items:center;justify-content:center}
.why-center .brand{font-size:28px}

/* testimonials */
.testimonials{top:2820px;height:400px}
.quote-card{position:absolute;top:140px;width:450px;height:180px;border:1px solid #e3e3e3;border-left:4px solid var(--blue);padding:24px 30px 0 60px}
.quote-card .mark{position:absolute;left:18px;top:18px;font-size:48px;font-weight:800;color:var(--blue);line-height:1}
.quote-card p{font-size:13px;color:var(--muted);font-style:italic;line-height:1.6}
.quote-card .who{margin-top:16px;font-size:12.5px;color:var(--blue);font-weight:700}
.quote-card .who small{display:block;color:var(--muted);font-weight:400}
.quote-card .stars{position:absolute;right:24px;bottom:30px;color:var(--yellow);font-size:16px;letter-spacing:2px}
.arrow{position:absolute;top:215px;color:#bbb;font-size:28px}
.testimonials .btn-blue{position:absolute;left:515px;top:340px}

/* cta */
.cta{top:3270px;height:300px;text-align:center}
.cta h2{font-size:32px;font-weight:800;color:var(--red);text-transform:uppercase}
.cta h3{font-size:32px;font-weight:800;text-transform:uppercase;line-height:1.2}
.cta .actions{margin-top:26px;display:flex;justify-content:center;gap:16px}

/* footer */
.site-footer{top:3570px;height:502px}
.footer-waves{position:absolute;left:0;top:0}
.footer-body{position:absolute;top:160px;width:100%;text-align:center;color:#fff}
.footer-body .brand{justify-content:center;color:#fff;font-size:36px}
.footer-nav{margin-top:40px;display:flex;justify-content:center;gap:34px;font-size:13px;font-weight:600}
.footer-contact{margin-top:30px;display:flex;justify-content:center;gap:60px;font-size:13px}
.copyright{position:absolute;bottom:0;width:100%;height:52px;background:var(--night);color:#aaa;font-size:12px;display:flex;align-items:center;justify-content:space-between;padding:0 40px}
.copyright .social span{width:22px;height:22px;background:#555}
</style>
</head>
<body>

<section class="hero">
  <div class="hero-photo" role="img" aria-label="Plumber at work on a job site, carrying a box of parts"></div>
  <div class="hero-shade"></div>
  <div class="hero-copy">
    <h1>Tired of waiting<br>for a plumber?</h1>
    <p>Call Us For Fast Response and Same Day Service</p>
    <span class="btn btn-blue">CALL US TODAY</span>
  </div>
  <form class="quote-form">
    <h2>GET A QUOTE</h2>
    <div class="field">Name</div>
    <div class="field">Email</div>
    <div class="field">Phone</div>
    <div class="field tall">Describe your issue</div>
    <span class="btn btn-red">SUBMIT INQUIRY</span>
  </form>
  <svg class="hero-wave" width="1200" height="200" viewBox="0 0 1200 200">
    <path d="M0 90 C250 20 500 160 800 80 C980 30 1100 60 1200 40 V200 H0Z" fill="#cde9f6"/>
    <path d="M0 130 C260 70 520 190 820 120 C1000 80 1110 100 1200 90 V200 H0Z" fill="#fff"/>
  </svg>
</section>

<header class="site-header">
  <div class="brand"><i></i>ClearFlow Plumbing</div>
  <div class="topbar">
    <span class="phone-ico"></span><span><b>CALL:</b> (555) 014-2280</span>
    <div class="social"><span></span><span></span><span></span><span></span></div>
  </div>
  <nav class="main-nav">
    <a>HOME</a><a>ABOUT US</a><a>SERVICES</a><a>TEAM</a><a>BLOG</a><a>CONTACT US</a>
    <span class="btn btn-red">GET A QUOTE</span>
  </nav>
</header>

<section class="features">
  <div class="feature">
    <div class="ico" style="background:var(--yellow)">
      <svg width="40" height="40" viewBox="0 0 40 40" fill="none" stroke="#fff" stroke-width="3"><path d="M6 26h20v-8h8"/><circle cx="12" cy="12" r="5"/></svg>
    </div>
    <h3>No-Dig Drain Repair</h3>
    <p>Trenchless fixes that keep your yard, drive and floors intact.</p>
  </div>
  <div class="feature">
    <div class="ico" style="background:var(--red)">
      <svg width="40" height="40" viewBox="0 0 40 40" fill="none" stroke="#fff" stroke-width="3"><path d="M8 32 L28 12"/><circle cx="30" cy="10" r="5"/></svg>
    </div>
    <h3>Repairs All Pipe Types</h3>
    <p>Copper, PEX, PVC, cast iron and galvanized lines handled.</p>
  </div>
  <div class="feature">
    <div class="ico" style="background:var(--blue)">
      <svg width="40" height="40" viewBox="0 0 40 40" fill="none" stroke="#fff" stroke-width="3"><circle cx="20" cy="20" r="13"/><path d="M20 12v9l6 4"/></svg>
    </div>
    <h3>Same Day Service</h3>
    <p>Call in the morning and our crew is at your door today.</p>
  </div>
</section>

<section class="about">
  <div class="about-copy">
    <h2>ABOUT <span>CLEARFLOW PLUMBING</span></h2>
    <p>We are a full service plumbing contractor serving homes and businesses across the valley. From drain cleaning and repairs to new construction, our licensed crew handles every job with care and modern equipment built for lasting results.</p>
    <p>Our focus is leak detection: under-slab and underground water service leaks found by acoustic, thermal and tracer gas methods, then repaired or rerouted. We clean drains fully with hydrojetters and chain knockers that scour the pipe wall to wall.</p>
    <span class="btn btn-blue">READ MORE</span>
  </div>
  <div class="about-video" role="img" aria-label="Video still of a technician repairing pipes under a sink">
    <svg width="70" height="70" viewBox="0 0 70 70"><circle cx="35" cy="35" r="33" fill="rgba(255,255,255,.85)"/><path d="M28 22 L50 35 L28 48Z" fill="var(--blue)"/></svg>
  </div>
</section>

<section class="services">
  <h2 class="section-title">Our <span>Services</span></h2>
  <svg class="title-rule" width="120" height="14" viewBox="0 0 120 14"><path d="M0 7H48M72 7H120" stroke="var(--blue)" stroke-width="2"/><circle cx="60" cy="7" r="5" fill="var(--blue)"/></svg>
  <div class="service-grid">
    <div class="service-card">
      <div class="photo" role="img" aria-label="Technician running a drain cleaning machine"></div>
      <h3>Drain Cleaning</h3>
      <p>Hydrojetting and chain knockers that clean the full pipe wall.</p>
      <div class="more"></div>
    </div>
    <div class="service-card">
      <div class="photo" role="img" aria-label="Pipe repair work inside a trench"></div>
      <h3>Repairs &amp; Reroutes</h3>
      <p>Lasting repairs and reroutes for failing supply and drain lines.</p>
      <div class="more"></div>
    </div>
    <div class="service-card">
      <div class="photo" role="img" aria-label="Leak detection equipment on a tiled floor"></div>
      <h3>Leak Detection</h3>
      <p>Acoustic, thermal and tracer gas tests for hidden slab leaks.</p>
      <div class="more"></div>
    </div>
    <div class="service-card">
      <div class="photo" role="img" aria-label="New construction plumbing rough-in"></div>
      <h3>New Construction</h3>
      <p>Complete plumbing for new homes, additions and commercial builds.</p>
      <div class="more"></div>
    </div>
  </div>
</section>

<section class="why" role="img" aria-label="Dark background of plumbing tools and equipment">
  <h2 class="section-title">Why Choose Us</h2>
  <svg class="why-map" width="1200" height="620" viewBox="0 0 1200 620">
    <g stroke="#fff" stroke-width="1.5" fill="none" opacity=".7">
      <path d="M500 230 L560 290"/><path d="M700 230 L640 290"/>
      <path d="M450 440 L480 410"/><path d="M750 440 L720 410"/>
    </g>
    <g fill="#fff">
      <circle cx="480" cy="210" r="30"/><circle cx="720" cy="210" r="30"/>
      <circle cx="430" cy="450" r="30"/><circle cx="770" cy="450" r="30"/>
    </g>
    <g fill="var(--blue)">
      <path d="M470 198h20v8a10 10 0 0 1-20 0z M477 216h6v6h5v4h-16v-4h5z"/>
      <path d="M706 212 l8-8 6 6 6-6 8 8 -14 12z"/>
      <rect x="420" y="438" width="20" height="24" rx="2"/>
      <circle cx="770" cy="443" r="7"/><path d="M756 465 a14 12 0 0 1 28 0z"/>
    </g>
  </svg>
  <div class="why-item left" style="left:200px;top:180px"><h3>Award Winning Services</h3><p>Trusted work recognized by local homeowners.</p></div>
  <div class="why-item" style="left:770px;top:180px"><h3>Year of Experience</h3><p>Decades of skill on every kind of plumbing.</p></div>
  <div class="why-item left" style="left:150px;top:420px"><h3>Projects Done</h3><p>Thousands of repairs and builds completed.</p></div>
  <div class="why-item" style="left:820px;top:420px"><h3>Qualified Staff</h3><p>Licensed, trained and insured technicians.</p></div>
  <div class="why-center"><div class="brand">ClearFlow</div></div>
</section>

<section class="testimonials">
  <h2 class="section-title">Customer <span>Testimonials</span></h2>
  <svg class="title-rule" width="120" height="14" viewBox="0 0 120 14"><path d="M0 7H48M72 7H120" stroke="var(--blue)" stroke-width="2"/><circle cx="60" cy="7" r="5" fill="var(--blue)"/></svg>
  <span class="arrow" style="left:90px">&#8249;</span>
  <div class="quote-card" style="left:130px">
    <span class="mark">&ldquo;</span>
    <p>"They found our slab leak in an hour and fixed it the same day. Clean work, fair price and a friendly crew from start to finish."</p>
    <div class="who">Dana Ruiz<small>Homeowner</small></div>
    <span class="stars">&#9733;&#9733;&#9733;&#9733;&#9733;</span>
  </div>
  <div class="quote-card" style="left:620px">
    <span class="mark">&ldquo;</span>
    <p>"Our main line kept backing up until they jetted it. Months later it still drains perfectly. I would call them again."</p>
    <div class="who">Mark Ellison<small>Restaurant owner</small></div>
    <span class="stars">&#9733;&#9733;&#9733;&#9733;&#9733;</span>
  </div>
  <span class="arrow" style="left:1095px">&#8250;</span>
  <span class="btn btn-blue">SEE MORE REVIEWS</span>
</section>

<section class="cta">
  <h2>Trusted Plumbing</h2>
  <h3>Contractors in the Rio Grande Valley</h3>
  <div class="actions"><span class="btn btn-blue">CALL US TODAY</span><span class="btn btn-red">GET A QUOTE</span></div>
</section>

<footer class="site-footer">
  <svg class="footer-waves" width="1200" height="450" viewBox="0 0 1200 450">
    <path d="M0 60 C300 0 600 110 900 50 C1050 20 1150 30 1200 20 V450 H0Z" fill="#bfe3f4"/>
    <path d="M0 100 C280 40 620 150 900 90 C1050 60 1140 70 1200 60 V450 H0Z" fill="#6cc2ea"/>
    <path d="M0 140 C300 80 620 190 920 130 C1060 105 1150 110 1200 105 V450 H0Z" fill="var(--blue)"/>
  </svg>
  <div class="footer-body">
    <div class="brand"><i style="background:#fff"></i>ClearFlow Plumbing</div>
    <nav class="footer-nav"><a>HOME</a><a>ABOUT US</a><a>SERVICES</a><a>TEAM</a><a>BLOG</a><a>CONTACT US</a></nav>
    <div class="footer-contact">
      <span>210 Harbor Lane, McAllen TX</span>
      <span>(555) 014-2280</span>
      <span>info@clearflowplumbing.com</span>
    </div>
  </div>
  <div class="copyright">
    <span>Copyright &copy; 2024 ClearFlow Plumbing. All Rights Reserved.</span>
    <div class="social"><span></span><span></span><span></span><span></span></div>
  </div>
</footer>

</body>
</html>
```